Facebook profile image design (Circle)

We require a Facebook profile image design for an event with a photo similar to the attached.

The event name is: Velmora Harbor Showcase & Gala 2022
Dat 7 - 8 October 2022

Colours: Gold, navy blue or black, white

file must be in pdf, png and ai

Target Market(s)

authors

Font styles to use
Serif

Requirements
Must have
• Author photo and book cover

```html
<!DOCTYPE html>
<html lang="en">
<head>
<meta charset="utf-8">
<title>Velmora Harbor Showcase &amp; Gala 2022 – Profile Badge</title>
<link rel="stylesheet" href="https://fonts.googleapis.com/css2?family=Montserrat:wght@500;600&family=Open+Sans:wght@700&family=Cinzel:wght@400&display=swap">
<style>
  :root {
    --page: #ffffff;
    --night: #231f20;
    --gold: #c9972a;
    --gold-light: #f2df5c;
    --cream: #fbf3d6;
    --navy: #1b5274;
    --sky: #5ea6dc;
    --sage: #6f9470;
    --white: #ffffff;
    --book-paper: #cfc2a3;
    --book-ink: #3a3226;
  }
  html, body {
    margin: 0;
    width: 1200px;
    height: 1200px;
    overflow: hidden;
    background: var(--page);
  }
  .canvas {
    position: relative;
    width: 1200px;
    height: 1200px;
  }
  .badge-art {
    position: absolute;
    inset: 0;
  }
  .event-name {
    position: absolute;
    left: 250px;
    top: 436px;
    width: 300px;
    text-align: center;
    font-family: "Montserrat", sans-serif;
    font-weight: 600;
    font-size: 46px;
    line-height: 1.02;
    letter-spacing: 1px;
    color: var(--gold);
    margin: 0;
  }
  .event-date {
    position: absolute;
    left: 250px;
    top: 580px;
    width: 300px;
    text-align: center;
    font-family: "Montserrat", sans-serif;
    font-weight: 500;
    font-size: 22px;
    letter-spacing: 1px;
    color: var(--white);
    margin: 0;
  }
  .book {
    position: absolute;
    left: 322px;
    top: 644px;
    width: 158px;
    height: 246px;
    background: linear-gradient(160deg, #ddd2b6 0%, var(--book-paper) 55%, #b7a98a 100%);
    box-shadow: 4px 4px 8px rgba(0,0,0,0.45);
    font-family: "Cinzel", serif;
    color: var(--book-ink);
    overflow: hidden;
  }
  .book-quote {
    position: absolute;
    top: 12px;
    left: 10px;
    right: 10px;
    margin: 0;
    font-family: "Montserrat", sans-serif;
    font-size: 4.3px;
    line-height: 1.4;
    text-align: center;
  }
  .book-title {
    position: absolute;
    top: 40px;
    left: 6px;
    right: 6px;
    margin: 0;
    font-size: 19px;
    line-height: 1.1;
    text-align: center;
    font-weight: 400;
  }
  .book-author-photo {
    position: absolute;
    left: 26px;
    top: 92px;
    width: 106px;
    height: 122px;
    background: linear-gradient(180deg, #b7a98a 0%, #2c3550 70%, #1e2740 100%);
  }
  .book-seal {
    position: absolute;
    left: 118px;
    top: 100px;
    width: 30px;
    height: 30px;
    border-radius: 50%;
    background: var(--gold);
  }
  .book-footer {
    position: absolute;
    left: 0;
    right: 0;
    bottom: 0;
    height: 32px;
    background: #1f2740;
    color: #e9e2cc;
    text-align: center;
  }
  .book-subtitle {
    margin: 4px 0 0;
    font-family: "Montserrat", sans-serif;
    font-size: 4.3px;
    letter-spacing: 0.3px;
    text-transform: uppercase;
  }
  .book-author {
    margin: 3px 0 0;
    font-size: 10px;
  }
</style>
</head>
<body>
<div class="canvas">
  <svg class="badge-art" width="1200" height="1200" viewBox="0 0 1200 1200">
    <defs>
      <linearGradient id="ringGradient" x1="200" y1="300" x2="1000" y2="800" gradientUnits="userSpaceOnUse">
        <stop offset="0" stop-color="var(--cream)"/>
        <stop offset="0.25" stop-color="var(--gold)"/>
        <stop offset="0.45" stop-color="var(--gold-light)"/>
        <stop offset="0.7" stop-color="var(--navy)"/>
        <stop offset="1" stop-color="var(--sky)"/>
      </linearGradient>
      <linearGradient id="bandGradient" x1="460" y1="960" x2="1000" y2="450" gradientUnits="userSpaceOnUse">
        <stop offset="0" stop-color="var(--gold)"/>
        <stop offset="0.25" stop-color="#e6d552"/>
        <stop offset="0.5" stop-color="var(--sage)"/>
        <stop offset="0.75" stop-color="var(--navy)"/>
        <stop offset="1" stop-color="var(--sky)"/>
      </linearGradient>
      <linearGradient id="portraitTone" x1="0" y1="0" x2="0" y2="1">
        <stop offset="0" stop-color="#d8d6c8"/>
        <stop offset="0.45" stop-color="#b88a74"/>
        <stop offset="0.75" stop-color="#c9c7b6"/>
        <stop offset="1" stop-color="#5f665f"/>
      </linearGradient>
      <clipPath id="stageClip">
        <circle cx="582" cy="578" r="372"/>
      </clipPath>
      <path id="bandArc" d="M 456 958 A 385 385 0 0 0 983 630"/>
    </defs>

    <circle class="badge-ring" cx="600" cy="600" r="399" fill="url(#ringGradient)"/>
    <circle class="badge-band" cx="600" cy="600" r="390" fill="url(#bandGradient)"/>
    <circle class="badge-inner-edge" cx="582" cy="578" r="380" fill="var(--cream)"/>
    <circle class="badge-stage" cx="582" cy="578" r="372" fill="var(--night)"/>

    <g clip-path="url(#stageClip)">
      <path class="author-portrait" role="img" aria-label="Portrait photograph of the author wearing a light headscarf and grey blazer"
            d="M 570 330 Q 700 290 820 330 Q 870 420 850 560 Q 950 620 990 700 L 990 960 L 483 960 L 483 720 Q 540 640 590 600 Q 560 440 570 330 Z"
            fill="url(#portraitTone)"/>
    </g>

    <text class="band-text" font-family="'Open Sans', sans-serif" font-weight="700" font-size="27" fill="var(--white)" letter-spacing="0.5">
      <textPath href="#bandArc" textLength="690" lengthAdjust="spacing">VELMORA HARBOR SHOWCASE &amp; GALA 2022</textPath>
    </text>
  </svg>

  <h1 class="event-name">VELMORA<br>HARBOR</h1>
  <p class="event-date">OCT. 7–8, 2022</p>

  <div class="book">
    <p class="book-quote">"A gentle, wise and honest guide for anyone starting over."<br>— Reader review, early edition</p>
    <h2 class="book-title">Embrace Your Detours</h2>
    <div class="book-author-photo" role="img" aria-label="Author photograph on the book cover"></div>
    <div class="book-seal"></div>
    <div class="book-footer">
      <p class="book-subtitle">A field guide to finding new roads forward</p>
      <p class="book-author">Marisol Tandang-Vehri</p>
    </div>
  </div>
</div>
</body>
</html>
```